Recruitment website for new startup company - Tal Brisk Recruitment

Hi , I need to design a web page for my new recruitment company with the ability to link to social media accounts. The ability to add and remove job posts along with a blog page which I can update. More importantly I need the website to have the functionality of applicants being able to upload their cv and somewhere for me to store it. I will need assistance/recommendation for email address with company name, hosting and security. An about us page. The website will also need a search function for applicants to narrow down the search. Again I will need to be able to update this myself as the company grows. I have my logo ready domain address ready and would like the web site done ASAP. Thank you for your help.
Updates

Project Deadline Extended
Reason: Want to get a few more ideas and variations to designs done. But using logo as inspiration Thanks

Target Market(s)

Financial and property industry so professionals. New starters to senior management age range 25-60

Industry/Entity Type

Financial

Coding

Coded - Design and coding required

Number of Pages Required

4 page

Colors

Designer to choose colors to be used in the design.

Requirements
Must have
• Ability for me to add amend and remove job posts, ability for applicants to upload cv and for me to store and access it. Link to social media accounts
Should not have
• Needs to be clean approachable so not to childish but must come across as approachable and trustworthy.
• No yellow please my logo has a gold V not yellow. If it looks yellow use a different colour please. Thanks

```html
<!DOCTYPE html>
<html lang="en">
<head>
<meta charset="utf-8">
<title>Tal Brisk Recruitment</title>
<link href="https://fonts.googleapis.com/css2?family=Open+Sans:wght@400;600;700&display=swap" rel="stylesheet">
<style>
:root{
  --navy:#2d4a7b;
  --navy-dark:#213a66;
  --ink:#1f3a68;
  --gold:#c39a2d;
  --grey-bg:#efeff1;
  --text:#444a55;
  --muted:#6a6f78;
  --white:#ffffff;
  --line:#e3e5ea;
}
*{box-sizing:border-box;margin:0;padding:0}
html,body{width:1200px;height:2462px;overflow:hidden}
body{position:relative;font-family:'Open Sans',Arial,sans-serif;color:var(--text);background:var(--white)}
.abs{position:absolute}

/* Hero */
.hero{left:0;top:0;width:1200px;height:509px;background:linear-gradient(180deg,#34507f 0%,#2d4a7b 60%,#2a4675 100%)}
.brand{left:131px;top:26px;color:var(--white);font-weight:600;font-size:20px;line-height:26px;letter-spacing:1px}
.brand small{display:block;font-size:12px;letter-spacing:3px;font-weight:600;line-height:18px}
.btn-login{left:922px;top:15px;width:63px;height:24px;border:1px solid var(--gold);color:var(--gold);font-size:11px;text-align:center;line-height:22px}
.btn-register{left:996px;top:15px;width:73px;height:24px;background:var(--gold);color:var(--white);font-size:11px;text-align:center;line-height:24px}
.nav{left:686px;top:53px;display:flex;gap:0;font-size:11px;font-weight:700;color:var(--white)}
.nav span{display:block;height:24px;line-height:24px;padding:0 11px}
.nav .active{background:var(--gold)}
.nav .about{margin-left:14px}
.nav .rec{margin-left:14px}
.nav .news{margin-left:15px}
.nav .contact{margin-left:15px}
.hero-title{left:0;width:1200px;top:168px;text-align:center;color:var(--white);font-size:31px;font-weight:600}
.hero-sub{left:0;width:1200px;top:214px;text-align:center;color:var(--white);font-size:14.5px}
.field{top:277px;height:43px;background:var(--white);display:flex;align-items:center;padding:0 12px;font-size:12px;color:#555}
.field svg{margin-right:8px;flex:none}
.field .chev{margin-left:auto;margin-right:0}
.btn-search{left:535px;top:369px;width:130px;height:41px;background:var(--gold);color:var(--white);font-weight:700;font-size:15px;text-align:center;line-height:41px}

/* Steps */
.sec-title{left:0;width:1200px;text-align:center;color:var(--ink);font-size:27px;font-weight:600}
.sec-title em{font-style:normal;color:var(--gold)}
.u-one{display:inline-block;border-bottom:2px solid var(--gold);line-height:1.35}
.steps-sub{left:0;width:1200px;top:618px;text-align:center;font-size:14px;color:var(--text)}
.step{top:691px;width:192px;height:163px;background:var(--white);box-shadow:0 1px 6px rgba(0,0,0,.15);text-align:center}
.step svg{position:absolute;left:74px;top:33px}
.step p{position:absolute;left:0;right:0;top:110px;font-weight:700;font-size:14px;color:var(--ink)}

/* Recent jobs */
.recent{left:0;top:921px;width:1200px;height:524px;background:var(--grey-bg)}
.rule{height:3px;width:54px;background:var(--gold);left:573px}
.arrow{top:1144px}
.job{top:1072px;width:297px;height:192px;background:var(--white)}
.job h3{position:absolute;left:24px;top:20px;font-size:12px;font-weight:700;color:var(--ink)}
.job .sep{position:absolute;left:0;right:0;top:53px;height:1px;background:var(--line)}
.job .loc{position:absolute;left:24px;top:73px;font-size:11.5px;color:var(--muted)}
.job .time{position:absolute;left:26px;top:94px;font-size:10.5px;color:var(--muted)}
.job .tag{position:absolute;right:17px;top:124px;height:16px;padding:0 10px;background:var(--navy);color:var(--white);font-size:9.5px;font-weight:600;letter-spacing:.5px;line-height:16px}
.job .band{position:absolute;left:0;right:0;bottom:0;height:54px;background:var(--navy)}
.job .pay{position:absolute;left:30px;top:14px;color:var(--gold);font-size:17px;font-weight:700}
.job .more{position:absolute;right:17px;top:13px;width:74px;height:24px;background:var(--gold);color:var(--white);font-size:10px;font-weight:700;text-align:center;line-height:24px}
.btn-all{left:524px;top:1331px;width:152px;height:41px;border:2px solid var(--gold);color:var(--gold);font-size:14px;font-weight:600;text-align:center;line-height:37px}

/* Featured */
.feat-img{top:1612px;width:297px;height:218px}
.feat-card{top:1802px;width:271px;height:201px;background:var(--white);box-shadow:0 1px 6px rgba(0,0,0,.15);padding:18px 16px}
.feat-card h4{font-size:12px;font-weight:700;color:var(--ink)}
.feat-card .loc{font-size:11.5px;color:var(--muted);margin-top:2px}
.feat-card .pay{font-size:13px;font-weight:700;color:var(--ink);margin-top:10px}
.feat-card .type{font-size:9.5px;font-weight:700;color:var(--gold);letter-spacing:1px;margin-top:6px}
.feat-card .desc{font-size:10.5px;line-height:16px;color:var(--text);margin-top:14px}
.feat-btn{top:1993px;width:74px;height:22px;background:var(--gold);color:var(--white);font-size:10px;font-weight:700;text-align:center;line-height:22px}

/* Footer */
.footer{left:0;top:2100px;width:1200px;height:362px;background:var(--navy)}
.f-brand{left:167px;top:2150px;color:var(--white);font-weight:600;font-size:22px;line-height:28px;letter-spacing:1px;text-align:center}
.f-brand small{display:block;font-size:13px;letter-spacing:3px;line-height:18px}
.f-follow{left:167px;width:124px;top:2233px;text-align:center;color:var(--white);font-size:12.5px;font-weight:700}
.social{top:2268px;width:30px;height:30px;border-radius:50%}
.f-head{top:2152px;color:var(--white);font-size:12.5px;font-weight:700}
.f-item{color:var(--white);font-size:10.5px;line-height:16px;display:flex;gap:14px;align-items:flex-start}
.f-menu{left:632px;top:2190px;color:var(--white);font-size:10.5px;line-height:16px}
.news-input{left:816px;top:2193px;width:256px;height:38px;background:var(--white);display:flex;align-items:center;padding-left:16px;font-size:12px;color:var(--navy);gap:10px}
.btn-signup{left:817px;top:2247px;width:102px;height:33px;background:var(--gold);color:var(--white);font-weight:700;font-size:14px;text-align:center;line-height:33px}
.f-rule{left:131px;top:2374px;width:938px;height:1px;background:#3e5b8c}
.copy{left:0;width:1200px;top:2412px;text-align:center;color:var(--white);font-size:10.5px}
</style>
</head>
<body>

<!-- Hero -->
<div class="abs hero" role="img" aria-label="Photo of job candidates seated in a waiting area, tinted blue"></div>
<div class="abs brand">TAL BRISK<small>RECRUITMENT</small></div>
<div class="abs btn-login">Login</div>
<div class="abs btn-register">Register</div>
<nav class="abs nav">
  <span class="active">HOME</span>
  <span class="about">ABOUT</span>
  <span class="rec">RECRUITMENT</span>
  <span class="news">NEWS</span>
  <span class="contact">CONTACT</span>
</nav>
<h1 class="abs hero-title">Multi Industry Recruitment Agency</h1>
<p class="abs hero-sub">Select your sector and / or type job keywords, then click search to find your perfect job</p>

<div class="abs field" style="left:250px;width:228px">
  <svg width="12" height="12" viewBox="0 0 12 12"><circle cx="5" cy="5" r="3.6" fill="none" stroke="#555" stroke-width="1.4"/><line x1="7.6" y1="7.6" x2="11" y2="11" stroke="#555" stroke-width="1.4"/></svg>Job Keywords
</div>
<div class="abs field" style="left:486px;width:228px">
  <svg width="10" height="13" viewBox="0 0 10 13"><path d="M5 12.5C2 8.5 1 6.8 1 5a4 4 0 0 1 8 0c0 1.8-1 3.5-4 7.5z" fill="none" stroke="#555" stroke-width="1.3"/><circle cx="5" cy="5" r="1.4" fill="#555"/></svg>Location
  <svg class="chev" width="12" height="8" viewBox="0 0 12 8"><path d="M1 1.5l5 5 5-5" fill="none" stroke="#444" stroke-width="1.6"/></svg>
</div>
<div class="abs field" style="left:722px;width:230px">
  <svg width="10" height="12" viewBox="0 0 10 12"><rect x="1" y="1" width="8" height="10" fill="none" stroke="#555" stroke-width="1.2"/><line x1="3" y1="4" x2="7" y2="4" stroke="#555"/><line x1="3" y1="6.5" x2="7" y2="6.5" stroke="#555"/></svg>Sector
  <svg class="chev" width="12" height="8" viewBox="0 0 12 8"><path d="M1 1.5l5 5 5-5" fill="none" stroke="#444" stroke-width="1.6"/></svg>
</div>
<div class="abs btn-search">SEARCH</div>

<!-- Steps -->
<h2 class="abs sec-title" style="top:562px">All the jobs you want in <em class="u-one">one</em> simple place</h2>
<p class="abs steps-sub">Find the jobs want in just a few simple quicks</p>

<div class="abs step" style="left:282px">
  <svg width="44" height="44" viewBox="0 0 44 44" fill="none" stroke="#c39a2d" stroke-width="2.2">
    <line x1="3" y1="6" x2="30" y2="6"/><line x1="3" y1="13" x2="18" y2="13"/><line x1="3" y1="20" x2="14" y2="20"/><line x1="3" y1="27" x2="14" y2="27"/><line x1="3" y1="34" x2="20" y2="34"/>
    <circle cx="28" cy="24" r="8"/><line x1="22" y1="30" x2="15" y2="38"/>
  </svg>
  <p>SEARCH</p>
</div>
<div class="abs step" style="left:504px">
  <svg width="44" height="44" viewBox="0 0 44 44" fill="none" stroke="#c39a2d" stroke-width="2.2">
    <path d="M24 6H5v34h34V21"/><path d="M36 4l5 5-18 18-7 2 2-7z"/><line x1="32" y1="8" x2="37" y2="13"/>
  </svg>
  <p>APPLY</p>
</div>
<div class="abs step" style="left:727px">
  <svg width="44" height="44" viewBox="0 0 44 44" fill="none" stroke="#c39a2d" stroke-width="2.2">
    <rect x="6" y="6" width="30" height="36" rx="2"/><rect x="15" y="2" width="12" height="7"/>
    <circle cx="21" cy="19" r="4"/><path d="M14 30c1-5 13-5 14 0"/><line x1="12" y1="36" x2="30" y2="36"/>
  </svg>
  <p>HIRED</p>
</div>

<!-- Recent jobs -->
<section class="abs recent"></section>
<h2 class="abs sec-title" style="top:971px">Recent <em>Jobs</em></h2>
<div class="abs rule" style="top:1019px"></div>

<svg class="abs arrow" style="left:68px" width="18" height="30" viewBox="0 0 18 30"><path d="M15 2L3 15l12 13" fill="none" stroke="#9aa0aa" stroke-width="2.5"/></svg>
<svg class="abs arrow" style="left:1108px" width="18" height="30" viewBox="0 0 18 30"><path d="M3 2l12 13L3 28" fill="none" stroke="#9aa0aa" stroke-width="2.5"/></svg>

<article class="abs job" style="left:131px">
  <h3>SALES &amp; MARKETING COORDINATOR</h3><div class="sep"></div>
  <p class="loc">Germany, Hanover</p><p class="time">65 days&nbsp;|&nbsp; 21:46:59</p>
  <span class="tag">FULL TIME</span>
  <div class="band"><span class="pay">£ 27500</span><span class="more">VIEW MORE</span></div>
</article>
<article class="abs job" style="left:451px">
  <h3>ENGINEERING TECHNICIAN</h3><div class="sep"></div>
  <p class="loc">Netherlands, Rotterdam</p><p class="time">65 days&nbsp;|&nbsp; 21:46:59</p>
  <span class="tag">FULL TIME</span>
  <div class="band"><span class="pay">£ 27500 - £ 30000</span><span class="more">VIEW MORE</span></div>
</article>
<article class="abs job" style="left:772px">
  <h3>SCIENCE TEACHER</h3><div class="sep"></div>
  <p class="loc">England, London,Comdon</p><p class="time">65 days&nbsp;|&nbsp; 21:46:59</p>
  <span class="tag">FULL TIME</span>
  <div class="band"><span class="pay">£ 30000 - £ 32500</span><span class="more">VIEW MORE</span></div>
</article>
<div class="abs btn-all">VIEW ALL JOBS</div>

<!-- Featured -->
<h2 class="abs sec-title" style="top:1502px">Featured <em>Job</em></h2>
<div class="abs rule" style="top:1544px;left:587px;width:40px"></div>

<div class="abs feat-img" style="left:131px;background:linear-gradient(135deg,#8a7d6c,#5b5a58 55%,#c9b89e)" role="img" aria-label="Photo of staff working at computers in an office"></div>
<div class="abs feat-img" style="left:451px;background:linear-gradient(135deg,#3a6f9a,#6d8fae 50%,#b04a3a)" role="img" aria-label="Photo of an engineer in a hard hat working on equipment"></div>
<div class="abs feat-img" style="left:772px;background:linear-gradient(135deg,#d9d3cc,#e8e2dc 50%,#8a5a45)" role="img" aria-label="Photo of a scientist examining a laboratory flask"></div>

<div class="abs feat-card" style="left:144px">
  <h4>STEAK HOUSE MANAGER</h4><p class="loc">Netherlands, Rotterdam</p>
  <p class="pay">£ 27500 - £ 30000</p><p class="type">FULL TIME</p>
  <p class="desc">Contrary to popular belief, Lorem Ips um is not simply random text. It has roots in a piece of classical Latin literature.</p>
</div>
<div class="abs feat-card" style="left:464px">
  <h4>STEAK HOUSE MANAGER</h4><p class="loc">Netherlands, Rotterdam</p>
  <p class="pay">£ 27500 - £ 30000</p><p class="type">FULL TIME</p>
  <p class="desc">Contrary to popular belief, Lorem Ips um is not simply random text. It has roots in a piece of classical Latin literature.</p>
</div>
<div class="abs feat-card" style="left:785px">
  <h4>STEAK HOUSE MANAGER</h4><p class="loc">Netherlands, Rotterdam</p>
  <p class="pay">£ 27500 - £ 30000</p><p class="type">FULL TIME</p>
  <p class="desc">Contrary to popular belief, Lorem Ips um is not simply random text. It has roots in a piece of classical Latin literature.</p>
</div>
<div class="abs feat-btn" style="left:171px">VIEW MORE</div>
<div class="abs feat-btn" style="left:491px">VIEW MORE</div>
<div class="abs feat-btn" style="left:812px">VIEW MORE</div>

<!-- Footer -->
<footer class="abs footer"></footer>
<div class="abs f-brand">TAL BRISK<small>RECRUITMENT</small></div>
<div class="abs f-follow">FOLLOW US</div>
<span class="abs social" style="left:177px;background:#2f5ca8"></span>
<span class="abs social" style="left:213px;background:#2aa3e0"></span>
<span class="abs social" style="left:248px;background:#3f8a96"></span>

<div class="abs f-head" style="left:407px">CONTACT US</div>
<div class="abs f-item" style="left:412px;top:2196px">
  <svg width="9" height="12" viewBox="0 0 10 13"><path d="M5 12.5C2 8.5 1 6.8 1 5a4 4 0 0 1 8 0c0 1.8-1 3.5-4 7.5z" fill="#fff"/><circle cx="5" cy="5" r="1.4" fill="#2d4a7b"/></svg>
  <span>418 Harbor Lane<br>Millbrook, MO 63800</span>
</div>
<div class="abs f-item" style="left:411px;top:2253px">
  <svg width="11" height="11" viewBox="0 0 12 12"><path d="M2.5 1l2 2.5-1.2 1.5c.8 1.6 2 2.8 3.7 3.7L8.5 7.5 11 9.5 9.5 11C5 10.5 1.5 7 1 2.5z" fill="#fff"/></svg>
  <span>555.010.2040</span>
</div>
<div class="abs f-item" style="left:411px;top:2297px">
  <svg width="12" height="10" viewBox="0 0 12 10"><rect x="0.5" y="0.5" width="11" height="9" fill="#fff"/><path d="M1 1l5 4 5-4" fill="none" stroke="#2d4a7b"/></svg>
  <span>info@talbrisk.com</span>
</div>

<div class="abs f-head" style="left:632px">MENU</div>
<div class="abs f-menu">Home<br>About Us<br>Recruitment<br>News<br>Contact Us</div>

<div class="abs f-head" style="left:816px">NEWSLETTER SIGNUP!</div>
<div class="abs news-input">
  <svg width="13" height="10" viewBox="0 0 12 10"><rect x="0.5" y="0.5" width="11" height="9" fill="none" stroke="#2d4a7b"/><path d="M1 1l5 4 5-4" fill="none" stroke="#2d4a7b"/></svg>
  E mail id
</div>
<div class="abs btn-signup">SIGNUP</div>

<div class="abs f-rule"></div>
<p class="abs copy">Copyrights @ 2017 All Rights Reserved</p>

</body>
</html>
```